Design New Vehicle Graphics for new company

We have 5 vehicles to get new vehicle raps on based on our new company name. BKT is it.
It stands for Brackmoor Pipe Systems.
Our website is brackmoorpipesystems.ie.
We have three KL haulettes
We have a KL Pelvano
We also have a KL Zint
All of these are to be wrapped.

I would like the followings texts to be used if possible.
Design Build Maintain
Water Pumps
Wastewater Pumps
Water Treatment
Irrigation
Water Softeners
Rainwater Harvesting
Leak Detection

Phone: 058 4417296
Website: brackmoorpipesystems.ie
Email: info@brackmoorpipesystems.ie

Target Market(s)

Everybody

Industry/Entity Type

Utilities

Requirements
Must have
• **The vehicles are in a dark grey and we want to incorporate this at the front so it is more of a half warp

```html
<!DOCTYPE html>
<html lang="en">
<head>
<meta charset="utf-8">
<title>Brackmoor Pipe Systems – Vehicle Wrap</title>
<link rel="stylesheet" href="https://fonts.googleapis.com/css2?family=Lexend:wght@400;500;600&display=swap">
<style>
  :root {
    --navy: #0d3b5e;
    --green: #0f4a1e;
    --charcoal: #3a3a3b;
    --charcoal-deep: #2b2b2c;
    --silver: #bdbdbd;
    --silver-light: #d6d6d6;
    --rear-white: #f4f4f4;
    --page: #f1f2f3;
    --page-rear: #dde0e3;
    --type-light: #e4e4e4;
  }
  html, body { margin: 0; padding: 0; overflow: hidden; }
  body { width: 800px; height: 1200px; background: var(--page); }
  .wrap-sheet { display: block; width: 800px; height: 1200px; font-family: "Lexend", sans-serif; }
  .rear-backdrop { fill: var(--page-rear); }
  .body-silver { fill: var(--silver); }
  .body-rear { fill: var(--rear-white); stroke: #c9c9c9; stroke-width: 1; }
  .front-charcoal { fill: var(--charcoal); }
  .sill-band { fill: var(--charcoal-deep); }
  .swoosh { fill: none; stroke: var(--navy); stroke-width: 3; }
  .door-split { stroke: #b0b0b0; stroke-width: 1; }
  .mark-ring { fill: var(--rear-white); stroke: var(--green); stroke-width: 5; }
  .mark-name { fill: var(--navy); font-weight: 600; font-size: 34px; text-anchor: middle; }
  .services { fill: var(--navy); font-size: 10px; font-weight: 500; }
  .bullet { fill: var(--navy); }
  .web { fill: var(--navy); font-size: 12px; font-weight: 500; }
  .name-side { fill: var(--type-light); font-size: 15px; font-weight: 500; }
  .name-rule { stroke: var(--type-light); stroke-width: 2; }
  .contact-side { fill: var(--type-light); font-size: 8px; }
  .phone-side { fill: var(--type-light); font-size: 11px; font-weight: 500; }
  .pillar { fill: var(--navy); font-size: 13px; font-weight: 600; }
  .pillar-icon { fill: none; stroke: var(--navy); stroke-width: 1.2; }
  .name-rear { fill: var(--navy); font-size: 18px; font-weight: 600; }
  .name-rule-rear { stroke: var(--navy); stroke-width: 2; }
  .contact-rear { fill: var(--navy); font-size: 12px; font-weight: 500; }
  .phone-rear { fill: var(--navy); font-size: 17px; font-weight: 500; }
  .web-rear { fill: var(--navy); font-size: 14px; font-weight: 500; }
  .icon-light { fill: var(--type-light); }
  .icon-navy { fill: var(--navy); }
</style>
</head>
<body>
<svg class="wrap-sheet" viewBox="0 0 800 1200" xmlns="http://www.w3.org/2000/svg">
  <defs>
    <path id="van-profile" d="M60,232 L60,178 Q70,150 110,136 L205,82 Q232,66 272,66 L705,66 Q726,66 729,92 L736,232 Q738,290 720,290 L72,290 Q60,290 60,272 Z"/>
    <clipPath id="clip-profile"><use href="#van-profile"/></clipPath>
  </defs>

  <!-- Rear backdrop -->
  <rect class="rear-backdrop" x="0" y="750" width="800" height="450"/>

  <!-- Driver side panel shapes -->
  <g class="side-left-shapes">
    <use href="#van-profile" class="body-silver"/>
    <g clip-path="url(#clip-profile)">
      <path class="front-charcoal" d="M0,0 L505,0 Q470,120 495,256 L0,256 Z"/>
      <rect class="sill-band" x="0" y="284" width="800" height="10"/>
    </g>
    <path class="swoosh" d="M230,262 Q300,242 370,258"/>
    <g class="mark">
      <circle class="mark-ring" cx="418" cy="190" r="62"/>
      <text class="mark-name" x="418" y="202">BKT</text>
    </g>
  </g>

  <!-- Driver side text -->
  <g class="side-left-text">
    <text class="contact-side" x="146" y="205">Contact Us</text>
    <circle class="icon-light" cx="121" cy="213" r="6"/>
    <text class="phone-side" x="130" y="217">(058) 4417296</text>
    <line class="name-rule" x1="225" y1="186" x2="225" y2="246"/>
    <text class="name-side" x="235" y="204">BRACKMOOR</text>
    <text class="name-side" x="235" y="221">PIPE</text>
    <text class="name-side" x="235" y="238">SYSTEMS</text>

    <g class="service-list">
      <circle class="bullet" cx="510" cy="88" r="3"/><text class="services" x="517" y="92">Wastewater Pumps &amp; Systems</text>
      <circle class="bullet" cx="514" cy="101" r="3"/><text class="services" x="521" y="105">Water Treatment &amp; Filtration</text>
      <circle class="bullet" cx="518" cy="114" r="3"/><text class="services" x="525" y="118">Well &amp; Water Pumps</text>
      <circle class="bullet" cx="522" cy="126" r="3"/><text class="services" x="529" y="130">Service &amp; Maintenance</text>
      <circle class="bullet" cx="526" cy="139" r="3"/><text class="services" x="533" y="143">Rainwater Harvesting</text>
      <circle class="bullet" cx="530" cy="151" r="3"/><text class="services" x="537" y="155">Water Mgmt</text>
      <circle class="bullet" cx="534" cy="164" r="3"/><text class="services" x="541" y="168">Leak Detection</text>
      <circle class="bullet" cx="538" cy="176" r="3"/><text class="services" x="545" y="180">Irrigation</text>
    </g>
    <circle class="icon-navy" cx="521" cy="196" r="4"/>
    <text class="web" x="528" y="200">www.brackmoorpipesystems.ie</text>
    <circle class="icon-navy" cx="521" cy="210" r="4"/>
    <text class="web" x="528" y="214">info@brackmoorpipesystems.ie</text>

    <g class="pillars">
      <circle class="pillar-icon" cx="250" cy="274" r="7"/><path class="pillar-icon" d="M246,270 L254,278 M254,270 L246,278"/>
      <text class="pillar" x="261" y="279">DESIGN</text>
      <circle class="pillar-icon" cx="367" cy="273" r="7"/><path class="pillar-icon" d="M363,277 L370,270"/>
      <text class="pillar" x="378" y="278">BUILD</text>
      <circle class="pillar-icon" cx="476" cy="271" r="7"/><path class="pillar-icon" d="M472,267 L480,275 M480,267 L472,275"/>
      <text class="pillar" x="487" y="276">MAINTAIN</text>
    </g>
  </g>

  <!-- Passenger side panel shapes (mirrored profile) -->
  <g class="side-right-shapes" transform="translate(802,357) scale(-1,1)">
    <use href="#van-profile" class="body-silver"/>
    <g clip-path="url(#clip-profile)">
      <path class="front-charcoal" d="M0,0 L505,0 Q470,120 495,256 L0,256 Z"/>
      <rect class="sill-band" x="0" y="284" width="800" height="10"/>
    </g>
    <path class="swoosh" d="M235,262 Q320,242 405,258"/>
  </g>
  <g class="mark">
    <circle class="mark-ring" cx="388" cy="548" r="62"/>
    <text class="mark-name" x="388" y="560">BKT</text>
  </g>

  <!-- Passenger side text -->
  <g class="side-right-text">
    <g class="service-list">
      <circle class="bullet" cx="142" cy="453" r="3"/><text class="services" x="148" y="457">Wastewater Pumps &amp; Systems</text>
      <circle class="bullet" cx="138" cy="466" r="3"/><text class="services" x="144" y="470">Water Treatment &amp; Filtration</text>
      <circle class="bullet" cx="135" cy="478" r="3"/><text class="services" x="141" y="482">Well &amp; Water Pumps</text>
      <circle class="bullet" cx="131" cy="491" r="3"/><text class="services" x="137" y="495">Service &amp; Maintenance</text>
      <circle class="bullet" cx="128" cy="503" r="3"/><text class="services" x="134" y="507">Rainwater Harvesting</text>
      <circle class="bullet" cx="124" cy="516" r="3"/><text class="services" x="130" y="520">Mechanical &amp; Electrical</text>
      <circle class="bullet" cx="121" cy="528" r="3"/><text class="services" x="127" y="532">Leak Detection</text>
      <circle class="bullet" cx="118" cy="541" r="3"/><text class="services" x="124" y="545">Irrigation</text>
    </g>
    <circle class="icon-navy" cx="104" cy="560" r="4"/>
    <text class="web" x="111" y="564">www.brackmoorpipesystems.ie</text>
    <circle class="icon-navy" cx="104" cy="575" r="4"/>
    <text class="web" x="111" y="579">info@brackmoorpipesystems.ie</text>

    <line class="name-rule" x1="476" y1="546" x2="476" y2="606"/>
    <text class="name-side" x="486" y="564">BRACKMOOR</text>
    <text class="name-side" x="486" y="581">PIPE</text>
    <text class="name-side" x="486" y="598">SYSTEMS</text>
    <text class="contact-side" x="620" y="566">Contact Us</text>
    <circle class="icon-light" cx="595" cy="573" r="6"/>
    <text class="phone-side" x="604" y="577">(058) 4417296</text>

    <g class="pillars">
      <circle class="pillar-icon" cx="254" cy="635" r="7"/><path class="pillar-icon" d="M250,631 L258,639 M258,631 L250,639"/>
      <text class="pillar" x="266" y="640">DESIGN</text>
      <circle class="pillar-icon" cx="372" cy="634" r="7"/><path class="pillar-icon" d="M368,638 L375,631"/>
      <text class="pillar" x="383" y="639">BUILD</text>
      <circle class="pillar-icon" cx="480" cy="635" r="7"/><path class="pillar-icon" d="M476,631 L484,639 M484,631 L476,639"/>
      <text class="pillar" x="491" y="640">MAINTAIN</text>
    </g>
  </g>

  <!-- Rear doors -->
  <g class="rear-panel">
    <path class="body-rear" d="M282,808 L518,808 Q540,810 548,850 L562,1070 L238,1070 L252,850 Q260,810 282,808 Z"/>
    <line class="door-split" x1="400" y1="808" x2="400" y2="1070"/>
    <line class="name-rule-rear" x1="287" y1="836" x2="287" y2="908"/>
    <text class="name-rear" x="298" y="860">BRACKMOOR</text>
    <text class="name-rear" x="298" y="881">PIPE</text>
    <text class="name-rear" x="298" y="902">SYSTEMS</text>
    <text class="contact-rear" x="312" y="930">Contact Us</text>
    <circle class="icon-navy" cx="274" cy="944" r="8"/>
    <text class="phone-rear" x="286" y="950">(058) 4417296</text>
    <g class="mark">
      <circle class="mark-ring" cx="476" cy="935" r="60"/>
      <text class="mark-name" x="476" y="947">BKT</text>
    </g>
    <circle class="icon-navy" cx="295" cy="1026" r="5"/>
    <text class="web-rear" x="304" y="1031">www.brackmoorpipesystems.ie</text>
    <circle class="icon-navy" cx="295" cy="1044" r="5"/>
    <text class="web-rear" x="304" y="1049">info@brackmoorpipesystems.ie</text>
  </g>
</svg>
</body>
</html>
```